International Medical Company Needs a Website Design for a Support Site

We need a website design for a support site we are doing for ostomates called Bright Rebounds. We are an international company but this website is for our Australian market.

The website is a support site for people who are living with an Ostomy or Bowel Disease. This is a site where they can read other ostomates' stories and how they are dealing with the fact that they have to wear a pouch everyday.

The URL for our US site is: http://www.brightrebounds-example.com/

We need to use the same logo but we have freedom around the color scheme. We are not fond of the brown color scheme used in our US site and are happy for designs to be submitted with alternatives.

• We want the design to be clean, inspiring, modern and inviting.
• We would like to see a design for the mainpage / homepage and one of the subpages
• We only require the PSD / image files (no HTML needed)

Attached to this project is our sitemap, an example wireframe and the logos. We are happy for you to play around with different options and don't have to stick to the layout shown in the wireframe.

If you have any further questions please ask.

```html
<!DOCTYPE html>
<html lang="en">
<head>
<meta charset="utf-8">
<title>Bright Rebounds</title>
<link href="https://fonts.googleapis.com/css2?family=Ubuntu:ital,wght@0,400;0,500;1,400&display=swap" rel="stylesheet">
<style>
:root{
  --page:#eeedf0;
  --text:#6a6a6a;
  --heading:#5f5f63;
  --rule:#c9c9cc;
  --accent:#6fcf4f;
  --footer:#364550;
  --footer-text:#e6e9ec;
}
*{margin:0;padding:0;box-sizing:border-box}
html,body{width:1200px;height:1115px;overflow:hidden}
body{background:var(--page);font-family:"Ubuntu",sans-serif;color:var(--text);position:relative}
.abs{position:absolute}
.section-title{font-size:19px;font-weight:500;color:var(--heading);line-height:24px}
.title-rule{width:37px;height:1px;background:var(--rule)}
.body-text{font-size:13.4px;line-height:22.5px}
.sub-title{font-size:15px;font-weight:500;color:var(--heading)}
.photo{border:2px solid #fff;box-shadow:0 0 0 1px #dcdcdf}
.story-name{font-size:13px;font-weight:500;color:var(--heading);line-height:16px}
.story-city{font-size:13px;line-height:16px}
.more-link{font-size:11px;font-weight:500;color:var(--heading);letter-spacing:.2px}
.accent-link{font-size:13px;font-weight:500;color:var(--accent)}
.article-title{font-size:15px;font-weight:500;color:var(--heading);line-height:20px}
.article-byline{font-size:13px;font-style:italic;line-height:18px}
.article-rule{width:201px;height:1px;background:var(--rule)}
.news-thumb{width:66px;height:66px}
.news-date{width:66px;height:26px;background:var(--accent);color:#fff;font-size:10px;font-weight:500;text-align:center;line-height:26px}
.news-date::before{content:"";position:absolute;left:28px;top:-5px;border-left:5px solid transparent;border-right:5px solid transparent;border-bottom:5px solid var(--accent)}
.news-title{font-size:15px;font-weight:500;color:var(--heading)}
.news-rule{width:268px;height:1px;background:var(--rule)}
.site-footer{left:0;top:1058px;width:1200px;height:57px;background:var(--footer);color:var(--footer-text);font-size:13px}
.footer-nav{right:116px;top:20px;display:flex;gap:28px;font-weight:500;font-size:13px}
</style>
</head>
<body>

<section class="intro">
  <h2 class="abs section-title" style="left:117px;top:69px">What is Bright Rebounds</h2>
  <div class="abs title-rule" style="left:118px;top:110px"></div>
  <p class="abs body-text" style="left:118px;top:128px;width:296px">Duis mollis, est non commodo luctus, nisi porttitor ligula, eget lacinia odio sem nec elit. Aenean eu leo quam. Pellentesque ornare sem lacinia quam. Aenean lacinia bibendum nulla sed consectetur. Nulla vitae elit libero, a pharetra augue. Phasellus turpis diam, dictum vitae venenatis non, mattis et nisl.</p>
  <p class="abs body-text" style="left:118px;top:308px;width:296px">In a nibh enim, vitae condimentum tellus. Aliquam tincidunt odio eu lectus scelerisque ut luctus sem cursus. Aliquam elementum, lacus id egestas aliquet, quam elit dapibus massa, at auctor tortor ante ut lacus. Aliquam tincidunt dictum lacinia. Donec risus eros, congue et lobortis ac, mattis nec neque.</p>
</section>

<section class="share">
  <h2 class="abs section-title" style="left:453px;top:69px">Share a story</h2>
  <div class="abs title-rule" style="left:454px;top:110px"></div>
  <p class="abs body-text" style="left:454px;top:128px;width:630px">Duis mollis, est non commodo luctus, nisi porttitor ligula, eget lacinia odio sem nec elit. Aenean eu leo quam. Pellentesque ornare sem lacinia quam. Aenean lacinia bibendum nulla sed consectetur. Nulla vitae elit libero, a pharetra augue. Phasellus turpis diam, dictum vitae venenatis.</p>
  <a class="abs accent-link" style="left:923px;top:208px">Share your story</a>

  <h3 class="abs sub-title" style="left:451px;top:232px">Featured stories</h3>
  <div class="abs photo" role="img" aria-label="Portrait of a smiling man in a suit in front of a brick wall" style="left:451px;top:272px;width:298px;height:148px;background:linear-gradient(90deg,#a25a3c 0%,#b8785a 35%,#8a6a5c 60%,#9b5b40 100%)"></div>
  <div class="abs story-name" style="left:451px;top:424px">Ned Calloway</div>
  <div class="abs story-city" style="left:451px;top:440px">Adelaida</div>

  <div class="abs photo" role="img" aria-label="Photo of a woman and a man in dress uniform standing together" style="left:783px;top:272px;width:300px;height:148px;background:linear-gradient(90deg,#4a3a22 0%,#6b5838 40%,#2e2a26 70%,#3d3428 100%)"></div>
  <svg class="abs" style="left:1046px;top:391px" width="16" height="16" viewBox="0 0 16 16" aria-hidden="true"><circle cx="8" cy="8" r="7" fill="#d9d9d9" opacity=".85"/><path d="M6 4.5v7l5.5-3.5z" fill="#444"/></svg>
  <div class="abs story-name" style="left:782px;top:424px">Marisa Dunmore</div>
  <div class="abs story-city" style="left:782px;top:440px">Melburne</div>
  <a class="abs more-link" style="left:1004px;top:450px">MORE STORIES</a>
</section>

<section class="tips">
  <h2 class="abs section-title" style="left:117px;top:531px">Tips for living</h2>
  <div class="abs title-rule" style="left:118px;top:572px"></div>
  <p class="abs body-text" style="left:118px;top:590px;width:628px">Duis mollis, est non commodo luctus, nisi porttitor ligula, eget lacinia odio sem nec elit. Aenean eu leo quam. Pellentesque ornare sem lacinia quam. Aenean lacinia bibendum nulla sed consectetur. Nulla vitae elit libero, a pharetra augue. Phasellus turpis diam, dictum vitae venenatis non, mattis et nisl. In a nibh enim, vitae condimentum tellus. Aliquam tincidunt odio eu lectus scelerisque ut luctus sem cursus.</p>

  <article>
    <h3 class="abs article-title" style="left:116px;top:707px">Finding Intimacy</h3>
    <div class="abs article-byline" style="left:116px;top:726px">by Nora Whitlaw</div>
    <p class="abs body-text" style="left:116px;top:756px;width:310px">Your ostomy doesn’t have to inhibit your love life. You can have an exciting, meaningful and fulfilling relationship. Here’s how.</p>
  </article>
  <div class="abs article-rule" style="left:117px;top:844px"></div>

  <article>
    <h3 class="abs article-title" style="left:449px;top:707px">No Guts, Still Glory</h3>
    <div class="abs article-byline" style="left:449px;top:726px">by Clara Westbrook Hale</div>
    <p class="abs body-text" style="left:449px;top:756px;width:310px">When asked what he thought this article should be titled, former football standout and S-pouch surgery alum Owen Tarrant didn’t hesitate...</p>
  </article>
  <div class="abs article-rule" style="left:450px;top:844px"></div>

  <article>
    <h3 class="abs article-title" style="left:116px;top:864px">Food, Glorious Food!</h3>
    <div class="abs article-byline" style="left:116px;top:883px">by Daphne Rourke, RD</div>
    <p class="abs body-text" style="left:116px;top:913px;width:310px">Whether it’s the turkey at Thanksgiving, potato pancakes at Hanukkah, or jambalaya for Kwanzaa, you can enjoy the season’s foods despite ostomy.</p>
  </article>

  <article>
    <h3 class="abs article-title" style="left:449px;top:864px">Triumphs &amp; Inspiration: Marathon Man</h3>
    <div class="abs article-byline" style="left:449px;top:883px">by Iris Fenwick</div>
    <p class="abs body-text" style="left:449px;top:913px;width:310px">Despite serious setbacks, former wrestler and J-pouch surgery survivor Gus Marlowe fought his way back happiness, one step at a time.</p>
  </article>
</section>

<section class="news">
  <h2 class="abs section-title" style="left:783px;top:531px">Latest news</h2>
  <div class="abs title-rule" style="left:784px;top:572px"></div>

  <div class="abs news-thumb" role="img" aria-label="Close-up of a silver trophy" style="left:783px;top:596px;background:linear-gradient(135deg,#3a2a24,#8a6a5a 50%,#2a1e1a)"></div>
  <div class="abs news-date" style="left:783px;top:672px">04 APR</div>
  <h3 class="abs news-title" style="left:866px;top:593px">Vestibulum turpis libero</h3>
  <p class="abs body-text" style="left:866px;top:620px;width:220px">Praesent commodo cursus magna, Maecenas faucibus mollis interdum. Praesent commodo cursus magna,</p>
  <div class="abs news-rule" style="left:799px;top:722px"></div>

  <div class="abs news-thumb" role="img" aria-label="Cyclist in racing kit by the seaside" style="left:783px;top:746px;background:linear-gradient(180deg,#8fb4d6,#b7c6d2 45%,#7a6a64 70%,#4a4a52)"></div>
  <div class="abs news-date" style="left:783px;top:822px">14 MAR</div>
  <h3 class="abs news-title" style="left:866px;top:743px">Fringilla Venenatis Cursus</h3>
  <p class="abs body-text" style="left:866px;top:770px;width:220px">Etiam porta sem malesuada magna mollis euismod. Donec ullamcorper nulla non metus auctor fringilla.</p>
  <div class="abs news-rule" style="left:799px;top:872px"></div>

  <div class="abs news-thumb" role="img" aria-label="Portrait of a smiling woman" style="left:783px;top:896px;background:linear-gradient(180deg,#6b4a36,#c79a80 55%,#e2c3b2)"></div>
  <div class="abs news-date" style="left:783px;top:972px">02 FEB</div>
  <h3 class="abs news-title" style="left:866px;top:893px">Vivamus antero convallis</h3>
  <p class="abs body-text" style="left:866px;top:920px;width:220px">Etiam porta sem malesuada magna mollis euismod. Donec ullamcorper nulla non metus auctor fringilla.</p>
</section>

<footer class="abs site-footer">
  <div class="abs" style="left:117px;top:20px">Copyright by Bright Rebounds 2014</div>
  <nav class="abs footer-nav">
    <a>LEGAL NOTICE</a>
    <a>PRIVACY POLICY</a>
    <a>SITEMAP</a>
  </nav>
</footer>

</body>
</html>
```